Meridale Networks, it support and management

We run an IT business, so techy style would work well. We need a re-design, now that we’ve moved and phone numbers have changed.

On the back of the card I like having something that helps with taking notes, like a grid or lines

The attachment is the current business card I am using.

We specialize in helping out in all kinds of support, including laptops, desktops, servers, and providing software solutions, like vexora 880, backups and ransomware prevention

Target Market(s)

Other small business owners, specifically smaller than 50 employees

Industry/Entity Type

SMB, but no specific niche

Contact Information for Business Card

I’d like the logo, name, my title/rolw, my contact details

Colors
0094D4
00A9DD
6FCCEA
C7EBF8
E9F6FB

Requirements
Must have
• The ability to take notes on the back of the card
Nice to have
• A new slogan or fun little quip, but not necessary
Should not have
• Street address of any kind.

```html
<!DOCTYPE html>
<html lang="en">
<head>
<meta charset="utf-8">
<title>Meridale Networks – Business Card</title>
<link href="https://fonts.googleapis.com/css2?family=Open+Sans:wght@400;600;700&display=swap" rel="stylesheet">
<style>
  :root {
    --backdrop: #232323;
    --card: #1e1f24;
    --card-edge: #2a2b31;
    --brand-blue: #0094d4;
    --brand-cyan: #00a9dd;
    --brand-sky: #6fccea;
    --brand-ice: #c7ebf8;
    --text-light: #e9f6fb;
    --emboss: #16171b;
    --emboss-light: #2c2d33;
    --note-line: rgba(111, 204, 234, 0.22);
  }
  * { box-sizing: border-box; margin: 0; padding: 0; }
  html, body {
    width: 1200px; height: 768px; overflow: hidden;
    background: var(--backdrop);
    font-family: "Open Sans", sans-serif;
  }
  .canvas {
    position: relative; width: 1200px; height: 768px;
    display: flex; align-items: center; justify-content: center; gap: 60px;
  }
  .card {
    position: relative; width: 500px; height: 286px;
    background: var(--card);
    border: 1px solid var(--card-edge);
    border-radius: 3px;
    box-shadow: 0 18px 40px rgba(0,0,0,.55);
    overflow: hidden;
  }

  /* Front */
  .brand {
    position: absolute; left: 34px; top: 30px;
    display: flex; align-items: center; gap: 8px;
  }
  .brand-dot {
    width: 12px; height: 12px; border-radius: 50%;
    background: var(--brand-blue);
  }
  .brand-name {
    color: var(--brand-blue); font-weight: 700; font-size: 26px; letter-spacing: .5px; line-height: 1.1;
  }
  .brand-sub {
    position: absolute; left: 54px; top: 66px;
    color: var(--brand-ice); font-size: 8px; letter-spacing: 1.6px; text-transform: uppercase;
  }
  .person {
    position: absolute; left: 34px; top: 104px;
    padding-left: 10px; border-left: 5px solid var(--brand-cyan);
  }
  .person-name { font-size: 24px; font-weight: 600; line-height: 1.1; }
  .person-name .first { color: var(--brand-sky); }
  .person-name .last { color: #fff; font-weight: 700; }
  .person-title { color: var(--text-light); font-size: 11px; margin-top: 3px; }
  .contacts {
    position: absolute; left: 34px; top: 170px;
    list-style: none; color: var(--text-light); font-size: 12px; line-height: 20px;
  }
  .contacts li { display: flex; align-items: center; gap: 8px; }
  .contacts svg { width: 11px; height: 11px; fill: var(--brand-cyan); flex: none; }
  .front-decoration {
    position: absolute; right: 26px; bottom: 22px;
    font-size: 50px; font-weight: 700; line-height: 1; color: var(--emboss);
    text-shadow: 0 1px 0 var(--emboss-light);
  }

  /* Back */
  .back-mark {
    position: absolute; left: 0; right: 0; top: 26px;
    display: flex; align-items: center; justify-content: center; gap: 10px;
  }
  .back-mark .brand-dot { width: 12px; height: 12px; background: var(--emboss); box-shadow: 0 1px 0 var(--emboss-light); }
  .back-mark .brand-name {
    color: var(--emboss); font-size: 30px;
    text-shadow: 0 1px 0 var(--emboss-light);
  }
  .notes {
    position: absolute; left: 34px; right: 34px; top: 92px; bottom: 30px;
    background-image: repeating-linear-gradient(
      to bottom,
      transparent 0, transparent 23px,
      var(--note-line) 23px, var(--note-line) 24px
    );
  }
  .notes-label {
    position: absolute; left: 34px; top: 74px;
    color: var(--brand-sky); font-size: 8px; letter-spacing: 1.6px; text-transform: uppercase;
  }
</style>
</head>
<body>
<main class="canvas">
  <section class="card card-front" aria-label="Card front">
    <div class="brand">
      <span class="brand-dot"></span>
      <span class="brand-name">Meridale</span>
    </div>
    <p class="brand-sub">Meridale Networks Inc</p>
    <div class="person">
      <p class="person-name"><span class="first">Jonah</span> <span class="last">Reeve</span></p>
      <p class="person-title">President</p>
    </div>
    <ul class="contacts">
      <li><svg viewBox="0 0 16 16"><path d="M3 1l3 3-2 2c1 2 3 4 5 5l2-2 3 3-2 3C6 15 1 10 0 3z"/></svg>555.014.2290 x 118</li>
      <li><svg viewBox="0 0 16 16"><path d="M4 0h8v16H4zM5 2v11h6V2z"/></svg>555.019.4471</li>
      <li><svg viewBox="0 0 16 16"><circle cx="8" cy="8" r="7"/></svg>www.meridalenet.com</li>
      <li><svg viewBox="0 0 16 16"><path d="M0 3h16v10H0zM1 4l7 5 7-5z"/></svg>jonah@meridalenet.com</li>
    </ul>
    <p class="front-decoration">Meridale</p>
  </section>

  <section class="card card-back" aria-label="Card back">
    <div class="back-mark">
      <span class="brand-dot"></span>
      <span class="brand-name">Meridale</span>
    </div>
    <p class="notes-label">Notes</p>
    <div class="notes" aria-label="Ruled lines for notes"></div>
  </section>
</main>
</body>
</html>
```